A building General Contractor is looking for a business card design

I need a business card designed. The company "Stoneridge Framing Contractors" is a general contractor for commercial buildings and pre-engineered metal buildings.

```html
<!DOCTYPE html>
<html lang="en">
<head>
<meta charset="utf-8">
<title>Stoneridge Framing Contractors — Business Card</title>
<link href="https://fonts.googleapis.com/css2?family=Arimo:wght@400;700&display=swap" rel="stylesheet">
<style>
  :root {
    --backdrop: #2a2a2a;
    --card: #0d0d0d;
    --ink: #ffffff;
    --ink-soft: #e6e6e6;
    --silver: #c9c9c9;
    --rule: #d8d8d8;
  }
  * { box-sizing: border-box; margin: 0; padding: 0; }
  html, body {
    width: 1200px; height: 1200px; overflow: hidden;
    background: var(--backdrop);
    font-family: "Arimo", Arial, sans-serif;
  }
  .sheet {
    width: 1200px; height: 1200px;
    display: flex; align-items: center; justify-content: center; gap: 70px;
  }
  .card {
    width: 400px; height: 640px;
    background: var(--card);
    border-radius: 26px;
    box-shadow: 0 14px 36px rgba(0,0,0,.45);
    display: flex; flex-direction: column; align-items: center;
    color: var(--ink);
    text-align: center;
  }
  .card--front { padding-top: 96px; }
  .card--back { justify-content: center; }

  .wordmark {
    font-weight: 700;
    text-transform: uppercase;
    line-height: 1.08;
    color: var(--ink);
  }
  .card--front .wordmark { font-size: 36px; letter-spacing: 1px; }
  .card--back .wordmark { font-size: 38px; letter-spacing: 1px; color: var(--silver); }
  .wordmark span { display: block; }

  .person { margin-top: 78px; }
  .person__name { font-size: 27px; font-weight: 700; letter-spacing: 1px; }
  .person__role { font-size: 15px; color: var(--ink-soft); margin-top: 4px; }

  .icon-row {
    display: flex; align-items: center; gap: 8px;
    margin-top: 14px; width: 300px;
  }
  .icon-row::before, .icon-row::after {
    content: ""; flex: 1; height: 1px; background: var(--rule);
  }
  .icon {
    width: 24px; height: 24px; border-radius: 5px; background: var(--ink);
    display: flex; align-items: center; justify-content: center;
  }
  .icon svg { width: 16px; height: 16px; }

  .contact { margin-top: 14px; font-size: 17px; line-height: 1.36; color: var(--ink-soft); }
  .divider { width: 250px; height: 1px; background: var(--rule); margin: 10px 0; }
  .address { font-size: 17px; line-height: 1.36; color: var(--ink-soft); }
</style>
</head>
<body>
<main class="sheet">
  <section class="card card--front">
    <div class="wordmark">
      <span>Stoneridge</span>
      <span>Framing</span>
      <span>Contractors</span>
    </div>

    <div class="person">
      <p class="person__name">MARTEN HALE</p>
      <p class="person__role">CEO/Founder</p>
    </div>

    <div class="icon-row">
      <span class="icon" aria-label="Mobile">
        <svg viewBox="0 0 16 16"><rect x="4.5" y="1.5" width="7" height="13" rx="1.5" fill="none" stroke="#000" stroke-width="1.6"/><circle cx="8" cy="12" r=".9" fill="#000"/></svg>
      </span>
      <span class="icon" aria-label="Telephone">
        <svg viewBox="0 0 16 16"><path d="M2 6c0-2 2-3 6-3s6 1 6 3l-2 1-1-2H5L4 7z" fill="#000"/><rect x="4" y="8" width="8" height="5" rx="1" fill="#000"/></svg>
      </span>
      <span class="icon" aria-label="Email">
        <svg viewBox="0 0 16 16"><rect x="2" y="4" width="12" height="8.5" rx="1" fill="#000"/><path d="M2.5 4.5 8 9l5.5-4.5" fill="none" stroke="#fff" stroke-width="1.2"/></svg>
      </span>
      <span class="icon" aria-label="Website">
        <svg viewBox="0 0 16 16"><circle cx="8" cy="8" r="6" fill="none" stroke="#000" stroke-width="1.5"/><path d="M2 8h12M8 2c-2.5 3-2.5 9 0 12M8 2c2.5 3 2.5 9 0 12" fill="none" stroke="#000" stroke-width="1.1"/></svg>
      </span>
    </div>

    <div class="contact">
      <p>+987 2210 6395</p>
      <p>+123 7781 4052</p>
      <p>info@stoneridgeframing.com</p>
      <p>www.stoneridgeframing.com</p>
    </div>
    <div class="divider"></div>
    <div class="address">
      <p>1450 W Harlan Avenue</p>
      <p>Crestfield County 4718</p>
    </div>
  </section>

  <section class="card card--back">
    <div class="wordmark">
      <span>Stoneridge</span>
      <span>Framing</span>
      <span>Contractors</span>
    </div>
  </section>
</main>
</body>
</html>
```